Buch-/eBook-Cover für Anbieter von Seminaren zu den Themen Deeskalation und Selbstschutz
Zielgruppe
Ich gebe mit KLW Seminare (KLW steht für Kraft Lebt Weiter) Seminare, überwiegend bei Behörden, Firmen, Institutionen und Rettungskräfte zu den Themen Deeskalation und Selbstschutz. Darüber hinaus gebe ich auch Vorträge zum o.g. Thema und biete Selbstverteidigungskurse u.a. für Frauen an. Zielgruppe des Buches sind grundsätzlich alle Menschen die sich unsicher fühlen. Nicht für Kinder, aber ab dem jugendlichen Alter aufwärts. Dieses Buchprojekt ist bereits mein zweites. Es gibt bereits ein Buch zu dem Thema, wobei das aktuelle Buchprojekt etwas 'tiefer' in die Materie geht. Das erste Buch heißt: Wanderer im offenen Gelände - Das Handbuch für gelassenes Auftreten in Streitmomenten www.klw-seminare.de
Aufgabenstellung
Das Farbkonzept von KLW (blau, orange, weiß) sollte erkennbar sein. (Wiedererkennung). Endformat des Buchs 12,5 x 19,0 cm, Umschlag: Softcover 4/4-farbig. https://www.papierwerk-blatt.de wird die Druckerei sein.
Buchtitel: Ruhe wohnt in dir selbst - Wie du Linien ziehst, Streit entschärfst und dich wappnest
Ich benötige nach dem Design die Daten, um sie an die Druckerei weiterzugeben. Geplant ist davon auch ein ebook. Ich benötige für den Druck den Buchdeckel vorne/hinten sowie Buchrücken und Strichcode mit ISBN-Nummer (wird gesondert übersandt) auf der Rückseite.
Das Design darf nicht zu überladen sein.

```html
<!DOCTYPE html>
<html lang="de">
<head>
<meta charset="utf-8">
<title>Ruhe wohnt in dir selbst – KLW Seminare</title>
<link rel="stylesheet" href="https://fonts.googleapis.com/css2?family=Bebas+Neue&family=Roboto:wght@400&display=swap">
<style>
  :root {
    --page-bg: #c07232;
    --cover-navy: #0b1f5e;
    --accent-orange: #d9822f;
    --circle-blue: #3f87a6;
    --figure-teal: #5fb8a8;
    --text-white: #f4f4f2;
  }
  * { margin: 0; padding: 0; box-sizing: border-box; }
  html, body {
    width: 1200px; height: 1200px; overflow: hidden;
    background: var(--page-bg);
  }
  .cover {
    position: absolute; left: 237px; top: 50px;
    width: 725px; height: 1100px;
    background: var(--cover-navy);
    border-top: 15px solid var(--accent-orange);
    border-bottom: 15px solid var(--accent-orange);
    overflow: hidden;
    font-family: "Bebas Neue", "Oswald", sans-serif;
  }
  .title {
    position: absolute; left: 52px; top: 30px; z-index: 3;
    line-height: 0.92; text-transform: uppercase; font-weight: 400;
  }
  .title-lead { display: block; font-size: 76px; color: var(--text-white); }
  .title-accent { display: block; font-size: 150px; color: var(--accent-orange); line-height: 0.9; }
  .title-end { display: block; font-size: 134px; color: var(--text-white); line-height: 0.9; }
  .website {
    position: absolute; left: 680px; top: 46px; z-index: 3;
    writing-mode: vertical-rl; transform: rotate(180deg);
    font-size: 18px; letter-spacing: 0.5px; color: var(--text-white);
  }
  .hero-circle { position: absolute; left: 100px; top: 331px; z-index: 1; }
  .hero-figures {
    position: absolute; left: 150px; top: 350px; z-index: 2;
    width: 440px; height: 600px;
    background: radial-gradient(closest-side ellipse at 50% 50%, rgba(217,130,47,0.85) 0%, rgba(217,130,47,0.55) 50%, rgba(95,184,168,0.2) 80%, rgba(95,184,168,0) 100%);
  }
  .subtitle {
    position: absolute; left: 55px; top: 974px; z-index: 3;
    font-size: 38px; line-height: 1.02; color: var(--text-white);
    text-transform: uppercase;
  }
  .subtitle-accent { color: var(--accent-orange); }
  .brand {
    position: absolute; left: 585px; top: 985px; z-index: 3;
    width: 130px; text-align: center;
  }
  .brand-mark { display: flex; align-items: center; justify-content: center; gap: 6px; }
  .brand-dot {
    width: 22px; height: 22px; border-radius: 50%;
    border: 2px solid var(--accent-orange);
  }
  .brand-name { font-size: 40px; color: var(--text-white); line-height: 1; }
  .brand-tagline {
    font-family: "Roboto", Arial, sans-serif;
    font-size: 11px; color: var(--text-white); margin-top: 4px;
  }
</style>
</head>
<body>
  <main class="cover">
    <h1 class="title">
      <span class="title-lead">Ruhe wohnt</span>
      <span class="title-accent">in dir</span>
      <span class="title-end">selbst</span>
    </h1>

    <p class="website">WWW.KLW-SEMINARE.DE</p>

    <svg class="hero-circle" width="522" height="522" viewBox="0 0 522 522" aria-hidden="true">
      <circle cx="261" cy="261" r="261" fill="var(--circle-blue)"/>
    </svg>

    <div class="hero-figures" role="img" aria-label="Illustration: zwei Personen, Frau und Mann, in orangefarbener Kleidung mit Mauerwerk-Muster, selbstbewusst mit Händen an den Hüften stehend"></div>

    <p class="subtitle">
      Wie du Linien ziehst, Streit<br>
      entschärfst und <span class="subtitle-accent">dich wappnest</span>
    </p>

    <div class="brand">
      <div class="brand-mark">
        <span class="brand-dot"></span>
        <span class="brand-name">KLW</span>
      </div>
      <div class="brand-tagline">Kraft Lebt Weiter</div>
    </div>
  </main>
</body>
</html>
```